A 'new law' boutique Australian law firm that provides specialist employment law and people managem

We value helping clients create results with respect workplaces. What differentiates us is we provide actionable training in understanding and dealing with people and ensure legal compliance fits with this approach. We would like a fresh approach to our training overview documents that we currently use in our current law firm (6 attached). Please use pictures, symbols etc consistent with our non-traditional law approach that captures the approach of each training session.. Attached is the logo and draft letterhead for Brook Legal which will launch soon.

Target Market(s)

HR Managers and in-house lawyers (non employment specialists) in mid-large Australian companies that are progressive with a relationship based approach to managing employee behaviours and disputes.

Industry/Entity Type

Human Resource

Font styles to use
Sans Serif

Colors
3176b5
33a6d7

Requirements
Must have
• 1 or 2 page PDF for each of the 6 documents that the wording supplied goes into your design which will be pretty similar as we want consistency with our documents

```html
<!DOCTYPE html>
<html lang="en">
<head>
<meta charset="utf-8">
<title>Contact Officer Training – Brook Legal</title>
<link rel="stylesheet" href="https://fonts.googleapis.com/css2?family=Montserrat:ital,wght@1,800;1,900&family=Open+Sans:wght@400;600;700;800&display=swap">
<style>
  :root {
    --blue: #3176b5;
    --blue-deep: #1d5fa8;
    --blue-navy: #0f3f86;
    --blue-sky: #33a6d7;
    --cell-light: #3f8ccb;
    --cell-dark: #1f6ab3;
    --ink: #2b2f36;
    --paper: #ffffff;
    --stage: #17191d;
  }
  * { box-sizing: border-box; margin: 0; padding: 0; }
  html, body { width: 1200px; height: 848px; overflow: hidden; }
  body {
    background: radial-gradient(ellipse at 50% 40%, #2a2d33 0%, var(--stage) 75%);
    font-family: "Open Sans", Arial, sans-serif;
    color: var(--ink);
    position: relative;
  }
  .flyer {
    position: absolute;
    left: 300px; top: 0;
    width: 600px; height: 848px;
    background: var(--paper);
    overflow: hidden;
  }
  .hero-photo {
    position: absolute; right: 0; top: 0;
    width: 300px; height: 180px;
    background: linear-gradient(90deg, rgba(255,255,255,1) 0%, rgba(226,222,214,.6) 30%, #b9a98f 70%, #7a5a3c 100%);
  }
  .title {
    position: absolute; left: 36px; top: 30px;
    font-family: "Montserrat", Arial, sans-serif;
    font-style: italic; color: var(--blue-deep);
    line-height: .9; text-transform: uppercase;
  }
  .title-top { font-size: 30px; font-weight: 800; letter-spacing: .5px; }
  .title-main { font-size: 64px; font-weight: 900; letter-spacing: 1px; }
  .band { position: absolute; left: 0; top: 134px; width: 600px; height: 50px; }
  .band-label {
    position: absolute; left: 36px; top: 141px;
    color: #fff; font-weight: 800; font-size: 13px; letter-spacing: .5px;
  }
  .need { position: absolute; font-size: 9px; line-height: 1.35; }
  .need p + p { margin-top: 6px; }
  .need-left { left: 36px; top: 180px; width: 270px; }
  .need-right { left: 322px; top: 200px; width: 244px; }
  .section-title {
    position: absolute; left: 36px;
    font-family: "Montserrat", Arial, sans-serif; font-style: italic; font-weight: 900;
    color: var(--blue-deep); text-transform: uppercase;
  }
  .overview-title { top: 318px; font-size: 19px; }
  .overview {
    position: absolute; left: 36px; top: 346px; width: 528px;
    border-collapse: collapse; color: #fff;
  }
  .overview td {
    border-bottom: 1px solid rgba(255,255,255,.7);
    font-size: 7.5px; line-height: 1.3; padding: 4px 8px; vertical-align: middle;
  }
  .overview .topic { background: var(--cell-light); width: 150px; font-size: 8.5px; }
  .overview .detail { background: var(--cell-dark); }
  .outcomes-title { top: 622px; font-size: 19px; }
  .outcomes { position: absolute; left: 36px; top: 650px; width: 370px; font-size: 9px; line-height: 1.35; }
  .outcomes-lead { font-weight: 700; margin-bottom: 3px; }
  .outcomes ol { list-style: none; }
  .brand {
    position: absolute; right: 36px; bottom: 50px;
    display: flex; align-items: center; gap: 8px;
    font-size: 26px; font-weight: 700; color: var(--blue-deep);
  }
  .brand-dot { width: 24px; height: 24px; border-radius: 50%; background: var(--blue-sky); }
  .foot-edge { position: absolute; left: 0; bottom: 0; width: 600px; height: 30px; }
</style>
</head>
<body>
<main class="flyer">
  <div class="hero-photo" role="img" aria-label="Photo of a wooden gavel resting on a law book in front of shelved legal volumes"></div>

  <h1 class="title">
    <span class="title-top">Contact Officer</span><br>
    <span class="title-main">Training</span>
  </h1>

  <svg class="band" viewBox="0 0 600 50" aria-hidden="true">
    <path d="M0 0 H330 C360 0 370 30 420 30 H600 V38 H420 C368 38 355 28 330 28 H0 Z" fill="var(--blue-navy)"/>
    <path d="M330 28 C355 28 368 38 420 38 H600 V42 H418 C366 42 352 32 330 32 H0 V28 Z" fill="var(--blue-sky)"/>
  </svg>
  <div class="band-label">TRAINING NEED</div>

  <div class="need need-left">
    <p>Unlawful or inappropriate behavior in the workplace that is left unaddressed can impact on productivity and employee retention. Claims can be costly in terms of time and money as well as the impact on mental health from being involved in uncomfortable adversarial processes.</p>
    <p>Clear policies and procedures explaining the organisation’s workplace behavior expectations and how grievances will be managed are a minimum compliance requirement.</p>
  </div>
  <div class="need need-right">
    <p>The challenge is ensuring that employees understand the directions contained in those policies, what is unlawful and inappropriate behaviour and the options available to address these behaviours if they experience them or engage in them.</p>
    <p>Well trained Contact Officers provide another resource to assist the organisation to provide a safe and respectful workplace.</p>
  </div>

  <h2 class="section-title overview-title">Overview</h2>
  <table class="overview">
    <tr><td class="topic">Discrimination</td><td class="detail">What is direct and indirect discrimination? What are the prescribed attributes? What are the exceptions to the general rules? Practical examples of behaviour that may be discriminatory.</td></tr>
    <tr><td class="topic">Harassment</td><td class="detail">What is harassment? Are protected attributes relevant to harassment? What is the difference between harassment and sexual harassment? How does the reasonable person test work in relation to harassment? Practical examples of behaviour that may be harassment or sexual harassment.</td></tr>
    <tr><td class="topic">Bullying</td><td class="detail">What is bullying. Explore how bullying differs to discrimination or inappropriate behaviour. Performance Management – when is it bullying and when is it not? Is all workplace conflict bullying? Practical examples of behaviour that may be bullying.</td></tr>
    <tr><td class="topic">Victimisation and Vilification</td><td class="detail">What is victimisation? What is vilification?</td></tr>
    <tr><td class="topic">Adverse Action</td><td class="detail">What is adverse action and how does it differ to other unlawful behaviour? What is a workplace right? When is it lawful to terminate employment because of an employee’s absence? How are the protected attributes relevant to adverse action?</td></tr>
    <tr><td class="topic">The Contact Officer’s role</td><td class="detail">How to perform your role when approached by an employee – the 6 step approach. What not to do. What are the obligations with regard to confidentiality?</td></tr>
    <tr><td class="topic">Grievance Options</td><td class="detail">Explore the options of complaint management – self management, internal informal management, formal internal management. How do they compare and what are the advantages and disadvantages of each approach. Is doing nothing an option? External options – advantages and disadvantages. Who decides which option?</td></tr>
    <tr><td class="topic">Test Learning</td><td class="detail">Role play, group discussion</td></tr>
  </table>

  <h2 class="section-title outcomes-title">Learning Outcomes</h2>
  <div class="outcomes">
    <p class="outcomes-lead">Training will enable participants to perform their role of Contact Officer and to understand:</p>
    <ol>
      <li>1 The role and responsibilities of a Contact Officer</li>
      <li>2 What amounts to unlawful workplace behaviour</li>
      <li>3 What is considered inappropriate behaviour in our workplace</li>
      <li>4 How to apply understanding unlawful/inappropriate behaviour to common scenarios</li>
      <li>5 How to address and resolve grievances early</li>
      <li>6 Options to resolve grievances internally and the Contact Officer role</li>
      <li>7 External options and their pros and cons for resolving grievances</li>
    </ol>
  </div>

  <div class="brand"><span class="brand-dot"></span><span>Brook Legal</span></div>

  <svg class="foot-edge" viewBox="0 0 600 30" aria-hidden="true">
    <rect x="0" y="14" width="600" height="16" fill="var(--blue-deep)"/>
    <rect x="0" y="10" width="600" height="4" fill="var(--blue-sky)"/>
  </svg>
</main>
</body>
</html>
```